Vexa Medical Aesthetics - Service Flyer

We are looking to have a friend-fold flyer designed that outlines all of the services offered. I am able to provide pricing on all products and outline of services.

We have had a flyer made in the past and the colours were black and white to go with the logo and keep it simple. We would prefer to keep these colours, but are open to adding in a couple of extra complimentary colours which would match our clinic. I have attached the original flyer that was created as well as our logo.

Target Market(s)

Women aged 25-65

Requirements
Must have
• Our website is www.vexaclinicdemo.com
• 555-014-2278
• Facebook: vexaclinic
• Instagram @vexaclinic
• Services to be included are:
• Some pricing has not been listed, but will update shortly
• Quenlix $8/unit
• Myrelt $10/unit
• Dermal Fillers
• (Cheeks, lips, jawline, chin, temples, under eyes, smile lines, smokers lines)
• 1ml syringe $475
• Mini Lip Plump $250
• Non-Surgical Face Lift $1100
• (Choice of 3 areas, eg. lips, jaw contouring, cheeks)
• Facial Treatments:
• Personalized Facial $85
• Organic Facial -$100
• Deep Cleansing / Acne Facial - $120
• Gel Peel (20% Glycolic/10% Lactic/3.2pH) - $75
• Dermaplaning $120
• Microdermabrasion $120
• Microneedling $250
• Microneedling (package of 3) $600
• Platelet-Rich Plasma (PRP) Facial $400
• Platinum Facial (Dermaplaning + Microneedling) $350
• LED Light Therapy $45
• High Frequency $45
• Skin Consultation (Free)
• Permanent Make-Up:
• Microblading $350
• Microblading Touch-Up $50
• Lashline Enhancement - Top Lashline $300
• Lashline Enhancement - Bottom Lashline $350
• Touch-Up Top/Bottom Lashline $50
• Lip Blush $450
• Lip Blush Touch-up $50
• Tattoo Removal $200 (per session)
• Cosmetic Treatments:
• Classic Eyelash Extensions $99
• Classic Fill $45
• Hybrid Eyelash Extensions $120
• Hybrid Fill $55
• Eyelash Lift & Tint $75
• Teeth Whitening $125
• Organic Teeth Whitening $150
• Medical Aesthetics Treatments:
• Laser Hair Removal $35 and up (per session)
• (Consultation and patch test required for all clients)
• Microneedling for Stretch Marks and Scars - $250 +
• Platelet-Rich Plasma (PRP) Hair Restoration - $500
• Scalp Micropigmentation - $500 and up
• The halvoray / laser hair removal write-up should be replaced with the following:
• We believe in providing only the best for our clients. We specialize in a number of Medical Aesthetics Treatments to address common skin and anti-aging concerns among our clients. All of our treatments are non-invasive, highly effective and affordable. Our services are performed by certified professionals, using clinically proven equipment and products approved and certified through Wellfield Bureau.
• We take pride in the high calibre experience we offer our clients and believe that choosing the appropriate certified professional that can deliver the results you desire, is of primary importance. Vexa employs highly qualified professionals, operating under Dr. Martin Okafor, Board Certified Plastic Surgeon acting as the Medical Director, as well as partners of the Tallowmere Medical team.

```html
<!DOCTYPE html>
<html lang="en">
<head>
<meta charset="utf-8">
<title>Vexa Medical Aesthetics – Service Flyer</title>
<link rel="stylesheet" href="https://fonts.googleapis.com/css2?family=Asap+Condensed:wght@400;700&family=Open+Sans:wght@400&display=swap">
<style>
  :root {
    --backdrop: #a3a3a3;
    --slate: #6d6d6e;
    --ink: #140c0c;
    --blush: #f08a82;
    --cream: #faf6ec;
    --paper: #ffffff;
    --muted: #8c8686;
    --rule: #d8d4d4;
    --condensed: "Asap Condensed", "Arial Narrow", sans-serif;
    --sans: "Open Sans", Arial, sans-serif;
  }
  * { box-sizing: border-box; margin: 0; padding: 0; }
  html, body { width: 817px; height: 1200px; overflow: hidden; }
  body { background: var(--backdrop); position: relative; font-family: var(--condensed); }

  .sheet { position: absolute; left: 69px; width: 693px; height: 490px; box-shadow: 0 2px 4px rgba(0,0,0,.25); }
  .sheet--outside { top: 67px; }
  .sheet--inside { top: 606px; }
  .panel { position: absolute; top: 0; height: 100%; overflow: hidden; }

  .photo { position: absolute; left: 0; width: 100%; }

  /* Outside */
  .panel--about { left: 0; width: 226px; background: var(--slate); }
  .panel--about .photo { top: 0; height: 162px; background: linear-gradient(135deg, #f1ddd0 0%, #d9b59c 50%, #a57e5f 100%); }
  .about-title { position: absolute; left: 24px; top: 172px; font-family: var(--sans); font-weight: 400; font-size: 19px; line-height: 24px; color: var(--blush); }
  .about-copy { position: absolute; left: 24px; top: 228px; width: 190px; font-size: 8.6px; line-height: 15.6px; color: #f2f2f2; }
  .about-copy p + p { margin-top: 15.6px; }

  .panel--contact { left: 226px; width: 233px; background: var(--ink); }
  .contact-list { position: absolute; left: 22px; top: 190px; height: 265px; writing-mode: vertical-rl; transform: rotate(180deg); list-style: none; font-family: var(--sans); font-size: 20px; line-height: 31px; color: var(--muted); }
  .contact-list li { white-space: nowrap; }
  .contact-list svg { width: 22px; height: 22px; margin-bottom: 8px; vertical-align: middle; }

  .panel--cover { left: 459px; width: 234px; background: var(--cream); }
  .panel--cover .photo { top: 0; height: 353px; background: linear-gradient(160deg, #f4f4f6 0%, #e6e8ee 55%, #c9dbe0 100%); }
  .cover-band { position: absolute; top: 353px; left: 0; width: 100%; height: 10px; background: var(--blush); }
  .wordmark { position: absolute; left: 0; top: 415px; width: 100%; text-align: center; font-family: var(--sans); font-size: 13px; letter-spacing: .5px; color: #111; }

  /* Inside */
  .panel--services { left: 0; width: 233px; background: var(--slate); color: #f4f4f4; }
  .panel--services .photo { top: 154px; height: 103px; background: linear-gradient(120deg, #f3e6df 0%, #e3c59f 55%, #c9a27c 100%); }
  .panel--menu { left: 233px; width: 233px; background: var(--ink); color: #f2f2f2; }
  .panel--menu .photo { top: 307px; height: 183px; background: linear-gradient(150deg, #e9eef2 0%, #c8d4dc 45%, #d7b9a6 100%); }
  .panel--medical { left: 466px; width: 227px; background: var(--paper); color: #333; }
  .panel--medical .photo { top: 128px; height: 362px; background: linear-gradient(160deg, #ece6ee 0%, #e5c9b9 55%, #cfa48d 100%); }

  .section { position: absolute; }
  .section-title { font-weight: 700; font-size: 17px; line-height: 20px; color: var(--blush); margin-bottom: 4px; }
  .price-list { list-style: none; font-size: 11px; line-height: 14.9px; }
  .price-row { display: flex; align-items: baseline; white-space: nowrap; }
  .price-row .leader { flex: 1; border-bottom: 0.6px solid currentColor; opacity: .8; margin: 0 2px; transform: translateY(-2px); }
  .price-row small, .note { font-size: 6.6px; }
  .note { line-height: 9px; margin-bottom: 2px; }

  .services { left: 17px; top: 16px; width: 275px; }
  .services .price-list { width: 206px; }
  .services .tight { width: 192px; }
  .facials { left: 17px; top: 262px; width: 202px; }
  .makeup { left: 82px; top: 16px; width: 202px; }
  .cosmetic { left: 82px; top: 172px; width: 202px; }
  .makeup, .cosmetic { left: 12px; }
  .medical { left: 10px; top: 16px; width: 197px; }
  .medical .section-title { font-size: 17px; }
</style>
</head>
<body>

<section class="sheet sheet--outside">
  <div class="panel panel--about">
    <div class="photo" role="img" aria-label="Photo of a relaxed woman resting at a spa with a flower in her hair"></div>
    <h2 class="about-title">Quality Matters:<br>The Vexa Experience</h2>
    <div class="about-copy">
      <p>We believe in providing only the best for our clients. We specialize in a number of Medical Aesthetics Treatments to address common skin and anti-aging concerns among our clients. All of our treatments are non-invasive, highly effective and affordable. Our services are performed by certified professionals, using clinically proven equipment and products approved and certified through Wellfield Bureau.</p>
      <p>We take pride in the high calibre experience we offer our clients and believe that choosing the appropriate certified professional that can deliver the results you desire, is of primary importance. Vexa employs highly qualified professionals, operating under Dr. Martin Okafor, Board Certified Plastic Surgeon acting as the Medical Director, as well as partners of the Tallowmere Medical team.</p>
    </div>
  </div>

  <div class="panel panel--contact">
    <ul class="contact-list">
      <li><svg viewBox="0 0 24 24" fill="none" stroke="currentColor" stroke-width="1.4"><circle cx="12" cy="12" r="10.5"/><path d="M8.5 7l2 2.2-1.2 1.6a7 7 0 003.9 3.9l1.6-1.2 2.2 2-1.2 1.5c-4 .2-8.6-4.4-8.4-8.4z"/></svg>555-014-2278</li>
      <li><svg viewBox="0 0 24 24" fill="none" stroke="currentColor" stroke-width="1.4"><circle cx="12" cy="12" r="10.5"/><ellipse cx="12" cy="12" rx="4.5" ry="10.5"/><path d="M1.5 12h21M3 7h18M3 17h18"/></svg>www.vexaclinicdemo.com</li>
      <li><svg viewBox="0 0 24 24" fill="none" stroke="currentColor" stroke-width="1.4"><circle cx="12" cy="12" r="10.5"/><rect x="8" y="6.5" width="8" height="11"/><path d="M8 6.5l8 11M16 6.5l-8 11"/></svg>info@vexaclinicdemo.com</li>
      <li><svg viewBox="0 0 24 24"><rect x="2" y="2" width="20" height="20" rx="3" fill="currentColor"/></svg>vexaclinic</li>
      <li><svg viewBox="0 0 24 24"><rect x="2" y="2" width="20" height="20" rx="3" fill="currentColor"/></svg>@vexaclinic</li>
    </ul>
  </div>

  <div class="panel panel--cover">
    <div class="photo" role="img" aria-label="Photo of a doctor in a white coat giving a cosmetic injection to a patient"></div>
    <div class="cover-band"></div>
    <p class="wordmark">Vexa Medical Aesthetics</p>
  </div>
</section>

<section class="sheet sheet--inside">
  <div class="panel panel--services">
    <div class="section services">
      <h2 class="section-title">Services</h2>
      <ul class="price-list">
        <li class="price-row">Quenlix<span class="leader"></span>$8/unit</li>
        <li class="price-row">Myrelt<span class="leader"></span>$10/unit</li>
        <li class="price-row">Dermal Fillers</li>
      </ul>
      <p class="note">(cheeks, lips, jawline, chin, temples, under eyes, smile lines, smokers lines)</p>
      <ul class="price-list tight">
        <li class="price-row">1ml syringe<span class="leader"></span>$475</li>
        <li class="price-row">Mini Lip Plump<span class="leader"></span>$250</li>
        <li class="price-row">Non-Surgical Face Lift<span class="leader"></span>$1100</li>
      </ul>
      <p class="note">(Choice of 3 areas, eg. lips, jaw contouring, cheeks)</p>
    </div>
    <div class="photo" role="img" aria-label="Photo of a technician applying eyelash extensions with tweezers"></div>
    <div class="section facials">
      <h2 class="section-title">Facial Treatments:</h2>
      <ul class="price-list">
        <li class="price-row">Personalized Facial<span class="leader"></span>$85</li>
        <li class="price-row">Organic Facial<span class="leader"></span>$100</li>
        <li class="price-row">Deep Cleansing / Acne Facial<span class="leader"></span>$120</li>
        <li class="price-row">Gel Peel (20% Glycolic/10% Lactic/3.2pH)<span class="leader"></span>$75</li>
        <li class="price-row">Dermaplaning<span class="leader"></span>$120</li>
        <li class="price-row">Microdermabrasion<span class="leader"></span>$120</li>
        <li class="price-row">Microneedling<span class="leader"></span>$250</li>
        <li class="price-row">Microneedling (package of 3)<span class="leader"></span>$600</li>
        <li class="price-row">Platelet-Rich Plasma (PRP) Facial<span class="leader"></span>$400</li>
        <li class="price-row">Platinum Facial&nbsp;<small>(Dermaplaning + Microneedling)</small><span class="leader"></span>$350</li>
        <li class="price-row">LED Light Therapy<span class="leader"></span>$45</li>
        <li class="price-row">High Frequency<span class="leader"></span>$45</li>
        <li class="price-row">Skin Consultation (Free)</li>
      </ul>
    </div>
  </div>

  <div class="panel panel--menu">
    <div class="section makeup">
      <h2 class="section-title">Permanent Make-Up:</h2>
      <ul class="price-list">
        <li class="price-row">Microblading<span class="leader"></span>$350</li>
        <li class="price-row">Microblading Touch-Up<span class="leader"></span>$50</li>
        <li class="price-row">Lashline Enhancement - Top Lashline<span class="leader"></span>$300</li>
        <li class="price-row">Lashline Enhancement - Bottom Lashline<span class="leader"></span>$350</li>
        <li class="price-row">Touch-Up Top/Bottom Lashline<span class="leader"></span>$50</li>
        <li class="price-row">Lip Blush<span class="leader"></span>$450</li>
        <li class="price-row">Lip Blush Touch-up<span class="leader"></span>$50</li>
        <li class="price-row">Tattoo Removal&nbsp;<small>(per session)</small><span class="leader"></span>$200</li>
      </ul>
    </div>
    <div class="section cosmetic">
      <h2 class="section-title">Cosmetic Treatments:</h2>
      <ul class="price-list">
        <li class="price-row">Classic Eyelash Extensions<span class="leader"></span>$99</li>
        <li class="price-row">Classic Fill<span class="leader"></span>$45</li>
        <li class="price-row">Hybrid Eyelash Extensions&nbsp;<small>(Couple)</small><span class="leader"></span>$120</li>
        <li class="price-row">Hybrid Fill&nbsp;<small>(Couple)</small><span class="leader"></span>$55</li>
        <li class="price-row">Eyelash Lift &amp; Tint<span class="leader"></span>$75</li>
        <li class="price-row">Teeth Whitening<span class="leader"></span>$125</li>
        <li class="price-row">Organic Teeth Whitening<span class="leader"></span>$150</li>
      </ul>
    </div>
    <div class="photo" role="img" aria-label="Photo of a woman receiving a facial skin treatment with a handheld device and serum dropper"></div>
  </div>

  <div class="panel panel--medical">
    <div class="section medical">
      <h2 class="section-title">Medical Aesthetics Treatments:</h2>
      <ul class="price-list">
        <li class="price-row">Laser Hair Removal (and up per session)<span class="leader"></span>$35</li>
      </ul>
      <p class="note">(Consultation and patch test required for all clients)</p>
      <ul class="price-list">
        <li class="price-row">Microneedling for Stretch Marks and Scars +<span class="leader"></span>$250</li>
        <li class="price-row">Platelet-Rich Plasma (PRP) Hair Restoration<span class="leader"></span>$500</li>
        <li class="price-row">Scalp Micropigmentation - and up<span class="leader"></span>$500</li>
      </ul>
    </div>
    <div class="photo" role="img" aria-label="Beauty portrait of a woman with smooth skin, hands resting near her face"></div>
  </div>
</section>

</body>
</html>
```